Guess The Score (UK Football Predictions) Website and SM Graphic.

Hi guys, we're looking for a smart graphic to advertise our upcoming 'GUESS THE SCORE' competition on our new website. The design needs to be square and look contemporary. It needs to have a blank space for football team names and times to be inserted (please see attached image) and it needs to say that the prize will be a best-selling Terrace Crowd t-shirt. We've attached a rough digital design, but it needs to look much smarter than this. We don't just want a slightly better version of it - it needs to look radically different, and in a good way. Smart fonts, sharp graphics, compelling yet easy on the eye. It needs to feature our logo (we can supply this). The letter 'O' in SCORE needs to be a football (maybe). We're gonna leave it to you to knock us out.

Target Market(s)

Sports Fans, Sports Bettors, Football/Soccer Fans

Font styles to use
Sans Serif

Requirements
Must have
• Contemporary feel. Eye-catching.
Nice to have
• Maybe some animation.
Should not have
• Mustn't be boring.

```html
<!DOCTYPE html>
<html lang="en">
<head>
<meta charset="utf-8">
<title>Guess the Score – Terrace Crowd</title>
<link rel="stylesheet" href="https://fonts.googleapis.com/css2?family=Graduate&family=Permanent+Marker&family=Cabin:wght@600;700&display=swap">
<style>
  :root{
    --page:#ffffff;
    --sky-top:#18243a;
    --sky-mid:#4d6a93;
    --haze:#9fbde2;
    --pitch:#2f8b2c;
    --pitch-dark:#072410;
    --title-green:#1f9a3c;
    --title-green-dark:#0c5a2a;
    --ink:#111111;
    --white:#ffffff;
    --accent-red:#e3141b;
    --board-blue:#2563a8;
    --board-blue-dark:#1b4d86;
    --silver:#c9cdd3;
    --tab-black:#1a1a1a;
  }
  *{margin:0;padding:0;box-sizing:border-box}
  html,body{width:1200px;height:929px;overflow:hidden;background:var(--page)}
  .canvas{position:relative;width:1200px;height:929px}
  .poster{
    position:absolute;left:167px;top:32px;width:865px;height:865px;overflow:hidden;
  }
  .stadium-scene{
    position:absolute;inset:0;
    background:
      radial-gradient(ellipse 70% 25% at 50% 42%, rgba(190,215,245,.55), transparent 70%),
      linear-gradient(180deg,var(--sky-top) 0%,var(--sky-mid) 28%,var(--haze) 48%,#6f8fb8 58%,var(--pitch) 62%,#236b22 80%,var(--pitch-dark) 100%);
  }
  .brand{
    position:absolute;right:26px;top:74px;display:flex;align-items:center;gap:8px;
    font-family:"Graduate",serif;font-size:19px;color:var(--white);
  }
  .brand-dot{width:14px;height:14px;border-radius:50%;background:var(--title-green)}
  .art{position:absolute;inset:0}
  .headline-guess{font-family:"Graduate",serif;font-size:150px}
  .headline-score{font-family:"Permanent Marker",cursive;fill:var(--ink)}
  .team-name{font-family:"Cabin",sans-serif;font-weight:700;font-size:30px;fill:var(--ink)}
  .match-time{font-family:"Cabin",sans-serif;font-weight:600;font-size:25px;fill:var(--white)}
  .vs{font-family:"Graduate",serif;font-size:40px;fill:var(--white)}
  .call-to-action{font-family:"Graduate",serif;font-size:30px;fill:var(--white)}
  .call-to-action .highlight{fill:var(--accent-red)}
</style>
</head>
<body>
<div class="canvas">
  <section class="poster">
    <div class="stadium-scene" role="img" aria-label="Floodlit football stadium at night with crowd stands, green pitch and a football in the foreground"></div>

    <div class="brand"><span class="brand-dot"></span>Terrace Crowd</div>

    <svg class="art" width="865" height="865" viewBox="0 0 865 865">
      <defs>
        <linearGradient id="guessFill" x1="0" y1="0" x2="0" y2="1">
          <stop offset="0" stop-color="var(--title-green)"/>
          <stop offset="1" stop-color="var(--title-green-dark)"/>
        </linearGradient>
        <linearGradient id="panelFill" x1="0" y1="0" x2="0" y2="1">
          <stop offset="0" stop-color="#ffffff"/>
          <stop offset="0.6" stop-color="#f2f3f5"/>
          <stop offset="1" stop-color="#c4c8ce"/>
        </linearGradient>
        <linearGradient id="tabFill" x1="0" y1="0" x2="0" y2="1">
          <stop offset="0" stop-color="#4a4a4a"/>
          <stop offset="0.5" stop-color="var(--tab-black)"/>
        </linearGradient>
      </defs>

      <!-- title -->
      <text class="headline-guess" x="228" y="222" textLength="412" lengthAdjust="spacingAndGlyphs" fill="url(#guessFill)" stroke="#e8eef2" stroke-width="2">GUESS</text>
      <text class="headline-score" x="170" y="327" font-size="40" textLength="80" lengthAdjust="spacingAndGlyphs">THE</text>
      <text class="headline-score" x="283" y="330" font-size="110" textLength="150" lengthAdjust="spacingAndGlyphs">SC</text>
      <circle cx="486" cy="287" r="40" fill="var(--white)" role="img" aria-label="Football forming the letter O"/>
      <text class="headline-score" x="524" y="330" font-size="110" textLength="170" lengthAdjust="spacingAndGlyphs">RE</text>

      <!-- match time tab -->
      <path d="M253 489 Q260 432 310 432 H555 Q605 432 612 489 Z" fill="var(--silver)"/>
      <path d="M267 489 Q272 440 318 440 H547 Q593 440 598 489 Z" fill="url(#tabFill)"/>
      <text class="match-time" x="432" y="468" text-anchor="middle">MATCH TIME</text>

      <!-- scoreboard bar -->
      <path d="M27 484 H837 Q835 578 780 578 H85 Q29 578 27 484 Z" fill="var(--silver)"/>
      <path d="M35 489 H829 Q826 573 776 573 H89 Q38 573 35 489 Z" fill="var(--board-blue)"/>
      <path d="M48 501 H340 V567 H90 Q50 567 48 501 Z" fill="url(#panelFill)"/>
      <path d="M522 501 H815 Q813 567 773 567 H522 Z" fill="url(#panelFill)"/>
      <path d="M335 501 H530 V540 Q530 572 500 572 H365 Q335 572 335 540 Z" fill="var(--silver)"/>
      <path d="M358 501 H507 V535 Q507 566 477 566 H388 Q358 566 358 535 Z" fill="var(--board-blue-dark)"/>
      <text class="team-name" x="194" y="548" text-anchor="middle">TEAM NAME 1</text>
      <text class="vs" x="432" y="553" text-anchor="middle">VS</text>
      <text class="team-name" x="663" y="548" text-anchor="middle">TEAM NAME 2</text>

      <!-- call to action -->
      <text class="call-to-action" x="220" y="747" textLength="424" lengthAdjust="spacingAndGlyphs">GUESS THE CORRECT SCORE</text>
      <text class="call-to-action" x="47" y="791" textLength="771" lengthAdjust="spacingAndGlyphs">AND <tspan class="highlight">WIN</tspan> A BEST-SELLING <tspan class="highlight">TERRACE CROWD</tspan> T-SHIRT</text>
    </svg>
  </section>
</div>
</body>
</html>
```